CoinHarborly.com Site Redesign

We are looking to redesign our CoinHarborly.com site. This site is focused on helping consumers make smart financial decisions. We provide reviews and articles in various categories.

We are looking for a responsive design to run on wordpress. We will also have adsense advertisements on our page and will want some ad spot space. We are thinking of two column design vs. single column.

Here is an example of what our competitors look like:
ShopperBeacon.org (mostly reviews vs. articles)
Homepage - https://www.shopperbeacon.org/
Category Review Listing - https://www.shopperbeacon.org/mortgage-refinance/best-mortgage-refinance
Individual Review - https://www.shopperbeacon.org/mortgage-refinance/c/brook-vale-mortgage-refinance-review

- I like that the site is extremely clean. I like the fixed header in mobile

PlumGuidely
Homepage - https://www.plumguidely.com/
Category Review Listing-https://www.plumguidely.com/auto_insurance/index.php
Individual Review- https://www.plumguidely.com/auto_insurance/zorvam_review.php

Articles - https://www.plumguidely.com/blog/2017/11/20/going-on-a-holiday-road-trip-be-prepared-for-these-hazards/

What I Like? I like the two column layout in that it gives room for advertising.
What I Do NOT Like? The top navigation is a little cumbersome and old. Mobile view is not very good. Content seems a bit cluttered.

KestoPurse
Homepage - https://www.kestopurse.com
Category Review Listing - https://www.kestopurse.com/blog/insurance/best-car-insurance-companies/?trk=kp_gn1_4.0
Individual Review- https://www.kestopurse.com/blog/insurance/torvel-insurance-review/

What I Like? very clean. Like the use of white space and focus on bright color call to action buttons.
What I Do NOT Like? In mobile a lot of content is pushed below the fold because of the large image above the fold. Reviews are not well organized.

Target Market(s)

consumers interested in saving money and making smart financial decisions

Industry/Entity Type

Financial

Logo Text

CoinHarborly.com or CoinHarborly

Coding

Coded - Design and coding required

Number of Pages Required

5+ page

Font styles to use
Sans Serif

Colors

Designer to choose colors to be used in the design.

Requirements
Must have
• -responsive design
• -room for ad space in the right column
Nice to have
• -good use of white space
• -clean layouts
Should not have
• -clutter

```html
<!DOCTYPE html>
<html lang="en">
<head>
<meta charset="utf-8">
<title>CoinHarborly.com – Make Smarter Financial Decisions</title>
<link href="https://fonts.googleapis.com/css2?family=Open+Sans:wght@400;600;700;800&display=swap" rel="stylesheet">
<style>
:root{
  --blue:#1a73c9;
  --blue-dark:#0f5aa3;
  --ink:#222a33;
  --muted:#6b7480;
  --line:#e2e6ea;
  --panel:#efefef;
  --footer:#f4f5f6;
  --bar:#2b2f35;
  --white:#ffffff;
}
*{box-sizing:border-box;margin:0;padding:0}
html,body{width:1200px;height:2568px;overflow:hidden}
body{font-family:"Open Sans",Arial,sans-serif;color:var(--ink);background:var(--white);position:relative}
a{color:inherit;text-decoration:none}

/* header */
.site-header{height:60px;display:flex;align-items:center;padding:0 24px;border-bottom:1px solid var(--line)}
.brand{display:flex;align-items:center;gap:8px;font-weight:800;font-size:22px;color:var(--blue)}
.brand-square{width:26px;height:26px;background:var(--blue)}
.main-nav{display:flex;gap:34px;margin-left:40px;font-size:15px;font-weight:600;color:var(--ink)}
.main-nav .active{color:var(--blue);border-bottom:2px solid var(--blue);padding-bottom:4px}
.social{margin-left:auto;display:flex;gap:12px}
.social span{width:32px;height:32px;border-radius:50%;border:2px solid var(--blue);display:block}

/* hero */
.hero{height:500px;position:relative;background:linear-gradient(120deg,#8a9096 0%,#b9bdc0 45%,#6f767d 100%);text-align:center;color:var(--white)}
.hero-title{padding-top:100px;font-size:52px;font-weight:800;letter-spacing:-.5px}
.hero-sub{font-size:30px;font-weight:700;margin-top:4px}
.finder{display:flex;justify-content:center;align-items:center;gap:18px;margin-top:36px;font-size:18px;font-weight:600}
.finder-select{width:300px;height:40px;background:var(--white);color:var(--muted);font-size:14px;text-align:left;padding:0 14px;display:flex;align-items:center;justify-content:space-between;border-radius:3px}
.dots{position:absolute;bottom:28px;left:0;right:0;display:flex;justify-content:center;gap:8px}
.dots span{width:10px;height:10px;border-radius:50%;background:rgba(255,255,255,.6)}
.dots span.on{background:var(--white)}

/* categories */
.categories{padding:48px 120px 0}
.cat-grid{display:grid;grid-template-columns:repeat(5,1fr);gap:20px}
.cat{height:124px;position:relative;display:flex;align-items:center;justify-content:center;color:var(--white);font-weight:700;font-size:15px;text-shadow:0 1px 3px rgba(0,0,0,.5)}
.c1{background:linear-gradient(135deg,#6b7c8a,#a9b4bc)}
.c2{background:linear-gradient(135deg,#9aa4ae,#5f6b76)}
.c3{background:linear-gradient(135deg,#7d8c9a,#c4c9cd)}
.c4{background:linear-gradient(135deg,#b7a99a,#6e6259)}
.c5{background:linear-gradient(135deg,#4e6f9a,#9db6d3)}
.c6{background:linear-gradient(135deg,#5c6670,#aeb6bd)}
.c7{background:linear-gradient(135deg,#8f9ba6,#4c5964)}
.c8{background:linear-gradient(135deg,#a7906f,#d8cbb5)}
.c9{background:linear-gradient(135deg,#6a7a87,#c5ccd2)}
.c10{background:linear-gradient(135deg,#3f5f86,#a0b7cf)}
.pager{display:flex;justify-content:flex-end;gap:8px;margin-top:18px}
.pager span{width:34px;height:34px;background:var(--blue);display:flex;align-items:center;justify-content:center}

/* content two columns */
.content{display:flex;gap:60px;padding:40px 120px 0 100px}
.main-col{width:660px}
.side-col{width:260px;display:flex;flex-direction:column;gap:12px}

.about{background:var(--panel);height:320px;padding:30px 30px 0;text-align:center}
.about h2{font-size:30px;font-weight:700}
.about-items{display:flex;justify-content:space-between;margin-top:26px}
.about-item{width:190px}
.about-icon{width:60px;height:60px;background:var(--blue);border-radius:6px;margin:0 auto 12px;display:flex;align-items:center;justify-content:center}
.about-item h3{font-size:15px;font-weight:700}
.about-item p{font-size:11px;color:var(--muted);margin-top:4px;line-height:1.45}

.recent{margin-top:100px}
.recent h2{font-size:30px;font-weight:700;margin-bottom:20px}
.cards{display:flex;gap:20px}
.card{width:320px}
.card-img{height:175px}
.img-a{background:linear-gradient(135deg,#6d8f6a,#c9d6c2)}
.img-b{background:linear-gradient(135deg,#7b8fa6,#d3dbe3)}
.card h3{font-size:17px;font-weight:700;margin-top:14px;line-height:1.3}
.card p{font-size:12px;color:var(--muted);margin-top:8px;line-height:1.55}
.read-more{display:inline-block;margin-top:8px;font-size:13px;font-weight:700;color:var(--blue)}
.recent .pager{justify-content:flex-start;margin:14px 0 0 230px}

.ad{width:260px}
.ad-tall{height:400px;background:linear-gradient(180deg,#f2f4f6 0%,#dfe6ee 60%,#1d4f8c 100%)}
.ad-mid{height:230px;background:linear-gradient(135deg,#1b1f26,#4a5360)}
.ad-low{height:220px;background:linear-gradient(135deg,#dfe3ea,#8fa3bf)}
.ad-gap{height:34px}

/* newsletter */
.newsletter{position:absolute;top:1980px;left:0;width:1200px;height:300px;background:linear-gradient(120deg,var(--blue-dark),var(--blue) 60%,#4a93d6);color:var(--white);text-align:center}
.newsletter h2{padding-top:78px;font-size:36px;font-weight:800}
.newsletter p{font-size:16px;margin-top:4px}
.subscribe{display:flex;justify-content:center;margin-top:22px}
.subscribe .field{width:420px;height:46px;background:var(--white);color:var(--muted);font-size:13px;display:flex;align-items:center;padding:0 16px;text-align:left}
.subscribe .btn{width:110px;height:46px;background:var(--blue-dark);border:2px solid var(--white);font-weight:700;display:flex;align-items:center;justify-content:center}

/* footer */
.site-footer{position:absolute;top:2280px;left:0;width:1200px;height:240px;background:var(--footer);padding:30px 24px 0;display:flex;gap:60px}
.site-footer h4{font-size:16px;font-weight:700;margin-bottom:14px;padding-bottom:8px;border-bottom:1px solid var(--line)}
.foot-all{width:820px}
.foot-cols{display:flex;gap:40px}
.site-footer ul{list-style:none;font-size:12px;color:var(--muted);width:180px}
.site-footer li{margin-bottom:8px}
.site-footer li::before{content:"» ";color:var(--blue)}
.bottom-bar{position:absolute;top:2520px;left:0;width:1200px;height:48px;background:var(--bar);color:#c8ccd1;font-size:12px;display:flex;align-items:center;justify-content:space-between;padding:0 24px}
</style>
</head>
<body>

<header class="site-header">
  <a class="brand" href="#"><span class="brand-square"></span>CoinHarborly.com</a>
  <nav class="main-nav">
    <a class="active" href="#">Home</a>
    <a href="#">Annuities</a>
    <a href="#">Auto Insurance</a>
    <a href="#">Credit Monitoring</a>
    <a href="#">Debt Management</a>
    <a href="#">Mortgages</a>
  </nav>
  <div class="social"><span></span><span></span></div>
</header>

<section class="hero" role="img" aria-label="Photo of people working together at a desk with laptops and paperwork">
  <h1 class="hero-title">Make Smarter Financial Decisions</h1>
  <p class="hero-sub">Find The Best Financial Products &amp; Services</p>
  <div class="finder">
    <span>I'm Looking For</span>
    <div class="finder-select">Choose Your Product / Category
      <svg width="10" height="6" viewBox="0 0 10 6"><path d="M0 0h10L5 6z" fill="#6b7480"/></svg>
    </div>
  </div>
  <div class="dots"><span></span><span class="on"></span><span></span></div>
</section>

<section class="categories">
  <div class="cat-grid">
    <a class="cat c1" href="#" role="img" aria-label="Annuities category photo">Annuities</a>
    <a class="cat c2" href="#" role="img" aria-label="Auto insurance category photo">Auto Insurance</a>
    <a class="cat c3" href="#" role="img" aria-label="Credit monitoring category photo">Credit Monitoring</a>
    <a class="cat c4" href="#" role="img" aria-label="Credit repair category photo">Credit Repair</a>
    <a class="cat c5" href="#" role="img" aria-label="Debt management category photo">Debt Management</a>
    <a class="cat c6" href="#" role="img" aria-label="Homeowners insurance category photo">Home Insurance</a>
    <a class="cat c7" href="#" role="img" aria-label="Identity theft category photo">Identity Theft</a>
    <a class="cat c8" href="#" role="img" aria-label="Life insurance category photo">Life Insurance</a>
    <a class="cat c9" href="#" role="img" aria-label="Mortgages category photo">Mortgages</a>
    <a class="cat c10" href="#" role="img" aria-label="Payday loans category photo">Payday Loans</a>
  </div>
  <div class="pager">
    <span><svg width="10" height="12" viewBox="0 0 10 12"><path d="M8 0L0 6l8 6z" fill="#fff"/></svg></span>
    <span><svg width="10" height="12" viewBox="0 0 10 12"><path d="M2 0l8 6-8 6z" fill="#fff"/></svg></span>
  </div>
</section>

<div class="content">
  <main class="main-col">
    <section class="about">
      <h2>What is CoinHarborly.com?</h2>
      <div class="about-items">
        <div class="about-item">
          <div class="about-icon"><svg width="34" height="34" viewBox="0 0 34 34" fill="none" stroke="#fff" stroke-width="3"><path d="M4 28l9-9 6 6 11-13"/><path d="M24 12h6v6"/></svg></div>
          <h3>We Analyze &amp; Explain</h3>
          <p>We analyze &amp; explain how each online service works</p>
        </div>
        <div class="about-item">
          <div class="about-icon"><svg width="34" height="34" viewBox="0 0 34 34" fill="#fff"><rect x="4" y="18" width="6" height="12"/><rect x="14" y="10" width="6" height="20"/><rect x="24" y="4" width="6" height="26"/></svg></div>
          <h3>We Test &amp; Compare</h3>
          <p>We test &amp; compare the leading services in each category</p>
        </div>
        <div class="about-item">
          <div class="about-icon"><svg width="34" height="34" viewBox="0 0 34 34" fill="#fff"><path d="M17 3l4.3 9 9.7 1.2-7.1 6.7 1.8 9.6L17 24.8l-8.7 4.7 1.8-9.6L3 13.2l9.7-1.2z"/></svg></div>
          <h3>We Review &amp; Rate</h3>
          <p>We review and rate each service to show which is best</p>
        </div>
      </div>
    </section>

    <section class="recent">
      <h2>Recent Articles</h2>
      <div class="cards">
        <article class="card">
          <div class="card-img img-a" role="img" aria-label="Photo of coins stacked beside a growing plant"></div>
          <h3>5 "Easy" Ways Parents Can Save $1000's a Year</h3>
          <p>Parents, lets face it – the high cost of raising children leaves us all needing a little extra money. Short of getting a big raise, switching jobs, or winning...</p>
          <a class="read-more" href="#">Read More »</a>
        </article>
        <article class="card">
          <div class="card-img img-b" role="img" aria-label="Photo of a motorcycle parked on a road"></div>
          <h3>Motorcycle Insurance Basics</h3>
          <p>Motorcycle insurance can be quite expensive. It can be the same amount as an auto insurance quote in some cases. Depending on the coverage you select...</p>
          <a class="read-more" href="#">Read More »</a>
        </article>
      </div>
      <div class="pager">
        <span><svg width="10" height="12" viewBox="0 0 10 12"><path d="M8 0L0 6l8 6z" fill="#fff"/></svg></span>
        <span><svg width="10" height="12" viewBox="0 0 10 12"><path d="M2 0l8 6-8 6z" fill="#fff"/></svg></span>
      </div>
    </section>
  </main>

  <aside class="side-col">
    <div class="ad ad-tall" role="img" aria-label="Advertisement space"></div>
    <div class="ad-gap"></div>
    <div class="ad ad-mid" role="img" aria-label="Advertisement space"></div>
    <div class="ad ad-low" role="img" aria-label="Advertisement space"></div>
  </aside>
</div>

<section class="newsletter" role="region" aria-label="Newsletter">
  <h2>Subscribe To Our Newsletter</h2>
  <p>Sign Up For The Latest Great Deals And Reviews</p>
  <div class="subscribe">
    <div class="field">Enter Your Email</div>
    <div class="btn">Submit</div>
  </div>
</section>

<footer class="site-footer">
  <div class="foot-all">
    <h4>All Services Reviewed</h4>
    <div class="foot-cols">
      <ul><li>Annuities</li><li>Auto Insurance</li><li>Credit Monitoring</li><li>Credit Repair</li><li>Debt Management</li></ul>
      <ul><li>Homeowners Insurance</li><li>Identity Theft</li><li>Life Insurance</li><li>Mortgages</li><li>Online Brokerages</li></ul>
      <ul><li>Payday Loans</li><li>Personal Finance</li><li>Student Loan Consolidation</li><li>Tax Settlement</li></ul>
    </div>
  </div>
  <div class="foot-popular">
    <h4>Popular Services Reviewed</h4>
    <ul><li>Debt Management</li><li>Payday Loans</li><li>Credit Cards</li></ul>
  </div>
</footer>

<div class="bottom-bar">
  <span>About us | Privacy Policy | Terms of Service | Contact Us</span>
  <span>Copyright © 2017 CoinHarborly. All rights reserved.</span>
</div>

</body>
</html>
```